LMT Vexa Website

Would like to have a website created that keeps with the branding of our other company; Harbor Ledger Corporation. www.harborledgerco.net

Target Market(s)

Medical providers, accounts receivable management

Industry/Entity Type

Accounts Receivable Management

Number of Pages Required

5+ page

Requirements
Must have
• look similar to www.harborledgerco.net, but will have different logo and domain as it is completely separate company

```html
<!DOCTYPE html>
<html lang="en">
<head>
<meta charset="utf-8">
<title>LMT Vexa — Accounts Receivable Management</title>
<link href="https://fonts.googleapis.com/css2?family=Merriweather:wght@400;700&family=Open+Sans:wght@400;600;700&display=swap" rel="stylesheet">
<style>
:root{
  --teal:#2f5d59;
  --teal-dark:#325d59;
  --maroon:#7c4a4a;
  --mint:#7db5a0;
  --slate:#7fa7ad;
  --charcoal:#464646;
  --page:#eeeeee;
  --ink:#333333;
  --sage:#7f9b95;
  --footer:#1c1c1c;
  --white:#ffffff;
}
*{margin:0;padding:0;box-sizing:border-box}
html,body{width:1200px;height:3709px;overflow:hidden}
body{background:var(--page);font-family:"Open Sans",sans-serif;color:var(--ink);position:relative}
.serif{font-family:"Merriweather",serif}
.abs{position:absolute}

/* header */
.site-header{position:absolute;left:0;top:0;width:1200px;height:92px;background:var(--page)}
.brand{position:absolute;left:110px;top:30px;font:700 36px "Open Sans",sans-serif;color:var(--teal);letter-spacing:2px}
.account{position:absolute;left:850px;top:18px;font:600 13px "Open Sans",sans-serif;color:var(--ink);display:flex;align-items:center;gap:6px}
.social-top{position:absolute;left:1000px;top:16px;display:flex;gap:9px}
.social-top span{width:20px;height:20px;border-radius:50%;background:#2c7fc9}
.divider{position:absolute;left:981px;top:14px;width:1px;height:24px;background:#bbb}
.main-nav{position:absolute;right:112px;top:58px;display:flex;gap:20px;font:600 15px "Open Sans",sans-serif;color:var(--teal)}

/* hero */
.hero{position:absolute;left:0;top:92px;width:1200px;height:660px;background:linear-gradient(100deg,#8d8a86 0%,#b3aea6 30%,#7a6b5d 60%,#a59b8d 100%);border-radius:0 0 170px 30px;overflow:hidden}
.hero-shade{position:absolute;inset:0;background:linear-gradient(180deg,rgba(40,40,40,.35),rgba(40,30,20,.25))}
.hero h1{position:absolute;left:0;width:1200px;top:170px;text-align:center;font:400 56px "Merriweather",serif;color:var(--white)}
.hero p{position:absolute;left:0;width:1200px;top:254px;text-align:center;font:400 21px/30px "Merriweather",serif;color:var(--white)}
.btn-pill{position:absolute;border-radius:30px;color:var(--white);text-align:center;font-weight:700}
.hero .btn-pill{left:516px;top:360px;width:168px;height:52px;line-height:52px;background:var(--teal);font-size:16px}

/* services */
.service{position:absolute;top:790px;text-align:center;font:700 21px/38px "Merriweather",serif;color:var(--ink)}
.service.active{color:var(--maroon)}

/* about */
.about-panel{position:absolute;left:0;top:910px;width:1200px;height:696px;background:var(--white);border-top-left-radius:170px}
.about-photo{position:absolute;left:110px;top:1020px;width:260px;height:485px;border-radius:0 243px 243px 0;background:linear-gradient(160deg,#b9c4c8,#8a8f92 50%,#5d5550)}
.about-title{position:absolute;left:470px;top:1002px;font:700 42px "Merriweather",serif;color:var(--teal)}
.about-text{position:absolute;left:470px;top:1077px;width:540px;font:400 17px/30px "Open Sans",sans-serif}
.pillar{position:absolute;top:1290px;width:200px}
.pillar svg{display:block;height:64px}
.pillar h3{margin-top:28px;font:700 20px "Merriweather",serif;color:var(--maroon)}
.pillar p{margin-top:10px;font:400 17px/30px "Open Sans",sans-serif}

/* how we work */
.process{position:absolute;left:0;top:1606px;width:1200px;height:770px;background:var(--teal-dark);color:var(--white)}
.process h2{position:absolute;left:0;width:1200px;top:70px;text-align:center;font:700 40px "Merriweather",serif}
.tabs{position:absolute;left:0;width:1200px;top:152px;display:flex;justify-content:center;gap:28px;font:400 21px "Open Sans",sans-serif}
.tabs .current{border-bottom:2px solid var(--white);padding-bottom:2px}
.tabs .muted{color:#a9bcb9}
.process p{position:absolute;left:200px;width:800px;top:230px;text-align:center;font:400 17px/30px "Open Sans",sans-serif}
.steps{position:absolute;left:0;top:0}

/* testimonials */
.testi-title{position:absolute;left:0;width:1200px;top:2448px;text-align:center;font:700 42px "Merriweather",serif;color:var(--teal)}
.review{position:absolute;top:2580px;width:330px;text-align:center}
.avatar{margin:0 auto;width:148px;height:148px;border-radius:50%;position:relative}
.quote-mark{position:absolute;left:-12px;top:6px;font:700 60px/1 "Merriweather",serif;color:#a05a55}
.review .who{margin-top:20px;font:400 19px "Merriweather",serif;color:#777}
.review .who b{color:var(--teal)}
.review blockquote{margin-top:18px;font:600 17px/30px "Open Sans",sans-serif;color:var(--ink)}

/* cta */
.cta{position:absolute;left:182px;top:3048px;width:836px;height:300px;background:var(--sage);color:var(--white)}
.cta h2{position:absolute;left:81px;top:80px;font:700 40px "Merriweather",serif}
.cta p{position:absolute;left:80px;top:154px;width:420px;font:400 17px/30px "Open Sans",sans-serif}
.cta .btn-pill{left:582px;top:118px;width:168px;height:54px;line-height:54px;background:var(--maroon);font:700 19px/54px "Merriweather",serif}

/* footer */
.site-footer{position:absolute;left:0;top:3340px;width:1200px;height:369px;background:var(--footer);border-top:8px solid var(--teal);border-right:8px solid var(--teal);border-radius:40px 220px 0 0;color:var(--white)}
.foot-brand{position:absolute;left:110px;top:100px;font:700 36px "Open Sans",sans-serif;letter-spacing:2px}
.foot-social{position:absolute;left:110px;top:180px;display:flex;gap:16px}
.foot-social span{width:30px;height:30px;border-radius:50%;background:#2c7fc9}
.legal{position:absolute;left:112px;top:244px;font:400 16px/30px "Open Sans",sans-serif}
.foot-h{position:absolute;font:700 17px "Merriweather",serif}
.email-field{position:absolute;left:476px;top:133px;width:196px;height:38px;border-radius:19px;background:var(--white);color:#888;font:400 15px/38px "Open Sans",sans-serif;padding-left:28px}
.submit{position:absolute;left:476px;top:190px;width:110px;height:38px;border-radius:19px;background:var(--teal);font:700 15px/38px "Open Sans",sans-serif;text-align:center}
.consent{position:absolute;left:476px;top:258px;font:400 15px "Open Sans",sans-serif;display:flex;align-items:center;gap:12px}
.consent i{width:14px;height:14px;background:var(--white);display:block}
.foot-list{position:absolute;font:400 15px/30px "Open Sans",sans-serif;list-style:none}
</style>
</head>
<body>

<header class="site-header">
  <div class="brand">LMT Vexa</div>
  <div class="account">
    <svg width="14" height="14" viewBox="0 0 14 14" fill="none" stroke="#333" stroke-width="1.3"><circle cx="7" cy="4.5" r="3"/><path d="M1.5 13.5c0-3 2.5-5 5.5-5s5.5 2 5.5 5"/></svg>
    MY ACCOUNT
  </div>
  <div class="divider"></div>
  <div class="social-top"><span></span><span></span><span></span></div>
  <nav class="main-nav"><span>HOME</span><span>PAY NOW</span><span>FOR CONSUMERS</span><span>CONTACT</span><span>ABOUT</span><span>CR BLOG</span></nav>
</header>

<section class="hero" role="img" aria-label="Photo of three colleagues discussing work around a table with a laptop">
  <div class="hero-shade"></div>
  <h1>Experience and Proven Results</h1>
  <p>sed do eiusmod tempor incididunt ut labore et dolore magna<br>aliquased do eiusmod tempor incididun</p>
  <div class="btn-pill">GET STARTED</div>
</section>

<div class="service" style="left:112px">Healthcare AR<br>Management</div>
<div class="service active" style="left:489px">Commercial AR<br>Management</div>
<div class="service" style="left:827px">Insurance Overpayment<br>Recovery</div>

<section class="about-panel"></section>
<div class="about-photo" role="img" aria-label="Photo of a woman with glasses talking in a meeting"></div>
<h2 class="about-title">About Us</h2>
<p class="about-text">Sed ut perspiciatis unde omnis iste natus error sit voluptatem accusantium doloremque laudantium, totam rem aperiam, eaque ipsa quae ab illo inventore veritatis et quasi architecto beatae vitae dicta sunt explicabo. Nemo enim ipsam voluptatem quia voluptas sit aspernatur aut odit aut fugit, sed quia consequuntur.</p>

<div class="pillar" style="left:468px">
  <svg width="66" height="64" viewBox="0 0 66 64" fill="none" stroke="#222" stroke-width="2"><circle cx="30" cy="34" r="26"/><circle cx="30" cy="34" r="17"/><circle cx="30" cy="34" r="8"/><path d="M30 34L60 16M52 12l2 8 8 2"/></svg>
  <h3>Our Mission</h3>
  <p>Neque porro quisq uam est, qui dolorem ipsum quia dolor sit amet.</p>
</div>
<div class="pillar" style="left:682px">
  <svg width="84" height="64" viewBox="0 0 84 64" fill="none" stroke="#222" stroke-width="2.4"><path d="M2 38c10-14 24-20 40-20s30 6 40 20c-10 14-24 20-40 20S12 52 2 38z"/><circle cx="42" cy="38" r="13"/><circle cx="42" cy="38" r="5"/><path d="M42 2v9M22 8l5 7M62 8l-5 7"/></svg>
  <h3>Our Vision</h3>
  <p>Neque porro quisq uam est, qui dolorem ipsum quia dolor sit amet.</p>
</div>
<div class="pillar" style="left:896px">
  <svg width="60" height="64" viewBox="0 0 60 64" fill="none" stroke="#222" stroke-width="1.8"><path d="M30 3v6M16 6l3 5M44 6l-3 5M14 16h32l10 12-26 32L4 28z"/><path d="M4 28h52M22 16l-6 12 14 32 14-32-6-12M30 16l-8 12M30 16l8 12"/></svg>
  <h3>Our Values</h3>
  <p>Neque porro quisq uam est, qui dolorem ipsum quia dolor sit amet.</p>
</div>

<section class="process">
  <h2>How we work</h2>
  <div class="tabs"><span class="current">EARLY OUT PROCESS</span><span class="muted">COLLECTIN PROCESS</span></div>
  <p>Ut enim ad minima veniam, quis nostrum exercitationem ullam corporis suscipit laboriosam, nisi ut aliquid ex ea commodi consequatur</p>
  <svg class="steps" width="1200" height="770" viewBox="0 1606 1200 770" font-family="Merriweather, serif" font-size="18" fill="#fff" text-anchor="middle">
    <g stroke="#fff" stroke-width="3">
      <polygon points="329,1953 439,2063 329,2173 219,2063" fill="var(--mint)"/>
      <polygon points="543,1953 653,2063 543,2173 433,2063" fill="var(--charcoal)"/>
      <polygon points="760,1953 870,2063 760,2173 650,2063" fill="var(--mint)"/>
      <polygon points="977,1953 1087,2063 977,2173 867,2063" fill="var(--charcoal)"/>
      <polygon points="216,2063 326,2173 216,2283 106,2173" fill="var(--maroon)"/>
      <polygon points="433,2063 543,2173 433,2283 323,2173" fill="var(--slate)"/>
      <polygon points="654,2063 764,2173 654,2283 544,2173" fill="var(--maroon)"/>
      <polygon points="868,2063 978,2173 868,2283 758,2173" fill="var(--slate)"/>
    </g>
    <text x="329" y="2038">Payment &amp;<tspan x="329" dy="30">Adjustment</tspan><tspan x="329" dy="30">applied</tspan></text>
    <text x="543" y="2056">A series of 3<tspan x="543" dy="30">bill are sent</tspan></text>
    <text x="760" y="2056">Emails are<tspan x="760" dy="30">sent weekly</tspan></text>
    <text x="977" y="2058">Account is moved<tspan x="977" dy="30">to collections</tspan></text>
    <text x="216" y="2162">Account is<tspan x="216" dy="30">Received</tspan></text>
    <text x="433" y="2162">First Clean bill<tspan x="433" dy="30">is sent</tspan></text>
    <text x="654" y="2148">Phone calls/<tspan x="654" dy="30">text messages</tspan><tspan x="654" dy="30">weekly</tspan></text>
    <text x="868" y="2156">If account not<tspan x="868" dy="30">resolved within</tspan><tspan x="868" dy="30">60 days</tspan></text>
  </svg>
</section>

<h2 class="testi-title">Testimonials</h2>
<div class="review" style="left:83px">
  <div class="avatar" role="img" aria-label="Portrait photo of Alice" style="background:linear-gradient(160deg,#c8d4dc,#8a6a55)"><span class="quote-mark">“</span></div>
  <p class="who"><b>Alice</b> / 6 months ago</p>
  <blockquote>“Nam libero tempore, cum soluta nobeligendi optio cumque nihil impedit&nbsp; maxime place”</blockquote>
</div>
<div class="review" style="left:430px">
  <div class="avatar" role="img" aria-label="Portrait photo of Sara" style="background:linear-gradient(160deg,#d7d2c9,#2f6d5e)"><span class="quote-mark">“</span></div>
  <p class="who"><b>Sara</b> / 6 months ago</p>
  <blockquote>“Nam libero tempore, cum soluta nobeligendi optio cumque nihil impedit&nbsp; maxime place”</blockquote>
</div>
<div class="review" style="left:777px">
  <div class="avatar" role="img" aria-label="Portrait photo of Jacob" style="background:linear-gradient(160deg,#dedede,#8e2a33)"><span class="quote-mark">“</span></div>
  <p class="who"><b>Jacob</b> / 6 months ago</p>
  <blockquote>“Nam libero tempore, cum soluta nobeligendi optio cumque nihil impedit&nbsp; maxime place”</blockquote>
</div>

<section class="cta">
  <h2>Start Saving Now</h2>
  <p>Nam libero tempore, cum soluta nobis est eligendi optio cumque nihil impedit quo minus id quod .</p>
  <div class="btn-pill">GET STARTED</div>
</section>

<footer class="site-footer">
  <div class="foot-brand">LMT Vexa</div>
  <div class="foot-social"><span></span><span></span><span></span></div>
  <p class="legal">2021 LMT Vexa. All Rights Reserved.<br>Privacy policy. Tearms &amp; conditions.</p>

  <div class="foot-h" style="left:476px;top:92px">SUBSCRIBE US</div>
  <div class="email-field">Email</div>
  <div class="submit">SUBMIT</div>
  <div class="consent"><i></i>yes, please contact me</div>

  <div class="foot-h" style="left:749px;top:94px">LINKS</div>
  <ul class="foot-list" style="left:754px;top:120px"><li>Home</li><li>Pay now</li><li>For consumer</li><li>About</li><li>CR Blog</li><li>Client login</li></ul>

  <div class="foot-h" style="left:916px;top:92px">CONTACT</div>
  <p class="foot-list" style="left:916px;top:120px">123 address goes here,<br>street name, vexa.</p>
  <p class="foot-list" style="left:916px;top:198px">hello@lmtvexa.com</p>
  <p class="foot-list" style="left:916px;top:246px">123-456-7890</p>
</footer>

</body>
</html>
```